BRASKETT LAND SERVICES BILLBOARD DESIGN

I NEED A BILLBOARD FOR MY BUSINESS. WE ARE A LAND CLEARING COMPANY AND I WOULD LIKE TO ADD A PICTURE OF MY TRACK LOADER TO THE SIGN. OPEN TO COLORS. I WOULD ALSO LIKE TO HAVE MY PHONE NUMBER 555-284-7196, WEBSITE WWW.BRASKETTLANDSERVICES.EXAMPLE, AND EMAIL ON THE SIGN (CONTACT@BRASKETTLANDSERVICES.EXAMPLE). DESIGNERS CAN HAVE THE FREEDOM TO DO WHATEVER STYLE THEY WANT AND TO USE ANY COLORS THEY WANT.

Target Market(s)

ANYONE WITH PROPERTY

Requirements
Must have
• PICTURE OF TRACK LOADER, WEBSITE, PHONE NUMBER, EMAIL
Nice to have
• OPEN TO ANYTHING
Should not have
• OPEN TO ANYTHING

```html
<!DOCTYPE html>
<html lang="en">
<head>
<meta charset="utf-8">
<title>Braskett Land Services Billboard</title>
<link rel="stylesheet" href="https://fonts.googleapis.com/css2?family=Saira+Condensed:wght@700;800&family=Montserrat:wght@600&display=swap">
<style>
  :root {
    --ink: #2a2a2a;
    --paper: #ffffff;
    --stage: #e9eaec;
    --foliage: #3f5a2c;
    --foliage-light: #6f8a4a;
    --grass: #9a8a55;
    --grass-dark: #7b6c3d;
  }
  * { margin: 0; padding: 0; box-sizing: border-box; }
  html, body {
    width: 1200px;
    height: 900px;
    overflow: hidden;
    background: var(--stage);
  }
  .billboard {
    position: absolute;
    left: 40px;
    top: 190px;
    width: 1120px;
    height: 520px;
    overflow: hidden;
    background: var(--ink);
    box-shadow: 0 6px 24px rgba(0,0,0,0.18);
  }
  .billboard-shapes {
    position: absolute;
    inset: 0;
    width: 1120px;
    height: 520px;
  }
  .copy {
    position: absolute;
    font-family: "Saira Condensed", "Arial Narrow", sans-serif;
    font-weight: 800;
    line-height: 0.95;
    white-space: nowrap;
  }
  .company-name {
    left: 30px;
    top: 34px;
    color: var(--paper);
    font-size: 56px;
    letter-spacing: 0.5px;
  }
  .call-now {
    left: 30px;
    top: 202px;
    color: var(--ink);
    font-size: 62px;
  }
  .phone {
    left: 30px;
    top: 260px;
    color: var(--ink);
    font-size: 66px;
    letter-spacing: 1px;
  }
  .email {
    left: 30px;
    top: 398px;
    color: var(--paper);
    font-family: "Montserrat", Arial, sans-serif;
    font-weight: 600;
    font-size: 18px;
    line-height: 1;
  }
  .website {
    left: 30px;
    top: 464px;
    color: var(--ink);
    font-size: 30px;
    font-weight: 700;
    letter-spacing: 0.3px;
  }
</style>
</head>
<body>
  <main class="billboard">
    <svg class="billboard-shapes" viewBox="0 0 1120 520" xmlns="http://www.w3.org/2000/svg">
      <defs>
        <linearGradient id="photo-tones" x1="0" y1="0" x2="0" y2="1">
          <stop offset="0" stop-color="var(--foliage-light)"/>
          <stop offset="0.45" stop-color="var(--foliage)"/>
          <stop offset="0.72" stop-color="var(--grass)"/>
          <stop offset="1" stop-color="var(--grass-dark)"/>
        </linearGradient>
      </defs>
      <path class="contact-band" d="M0,195 C180,182 340,160 600,146 L600,330 C360,332 180,346 0,376 Z" fill="var(--paper)"/>
      <path class="footer-band" d="M0,446 C200,436 380,418 640,396 L640,520 L0,520 Z" fill="var(--paper)"/>
      <path class="curve-gap" d="M554,0 C364,170 364,350 584,520 L1120,520 L1120,0 Z" fill="var(--paper)"/>
      <path class="curve-stripe" d="M548,0 C358,170 358,350 578,520" fill="none" stroke="var(--ink)" stroke-width="16"/>
      <path class="loader-photo" role="img" aria-label="Photo of a tracked loader with a forestry mulcher clearing brush on a grassy hillside in front of oak trees" d="M590,0 C400,170 400,350 620,520 L1120,520 L1120,0 Z" fill="url(#photo-tones)"/>
    </svg>

    <h1 class="copy company-name">BRASKETT<br>LAND SERVICES</h1>
    <p class="copy call-now">CALL NOW</p>
    <p class="copy phone">555-284-7196</p>
    <p class="copy email">contact@braskettlandservices.example</p>
    <p class="copy website">WWW.BRASKETTLANDSERVICES.EXAMPLE</p>
  </main>
</body>
</html>
```